Diabetes Education Flyer Design Project

We need a 8.5" X 11" flyer design for a retail pharmacy located in Queens, NYC to promote our new program of "Free Diabetes Education". This flyer will be distributed to doctors offices and to places where people congregate. The flyer should create a fear to the audience about diabetes and an urgency to come or call the pharmacy to get more information on the "Free Diabetes Education". The target audience is 40+ years old with national background of West Indies and India. They are mostly blue color worker with a highschool or less education

Target Market(s)

People with diabetes aging 40+, from West Indies and India, low literacy level

Industry/Entity Type

Education

Requirements
Must have
• Must have graphics and colors to attract the targetted age/race/literacy. Must have graphics and colors to create fear at the begining and hope at the end.
Nice to have
• Fonts to support the theme

```html
<!DOCTYPE html>
<html lang="en">
<head>
<meta charset="utf-8">
<title>Free Education for Diabetics – Oakline Pharmacy</title>
<link rel="stylesheet" href="https://fonts.googleapis.com/css2?family=Cinzel:wght@700&family=Arimo:wght@400;700&display=swap">
<style>
  :root {
    --page: #eeeeee;
    --stone-dark: #6f6a62;
    --stone-mid: #a29c90;
    --stone-light: #c9c4b8;
    --veil: rgba(255,255,255,0.42);
    --veil-strong: rgba(255,255,255,0.72);
    --alarm-red: #c8262c;
    --brand-magenta: #e0197d;
    --brand-blue: #2b3f8f;
    --hope-cyan: #33c1dc;
    --ink: #111111;
    --xray-dark: #1b1b1b;
    --xray-bone: #9a9a9a;
  }
  * { margin: 0; padding: 0; box-sizing: border-box; }
  html, body { width: 958px; height: 1200px; overflow: hidden; background: var(--page); }
  .flyer {
    position: relative; width: 958px; height: 1200px; background: var(--page);
    font-family: "Arimo", Arial, sans-serif; color: var(--ink);
  }
  .stone-backdrop {
    position: absolute; left: 20px; top: 20px; width: 918px; height: 1160px;
    background: radial-gradient(ellipse at 50% 40%, var(--stone-light), var(--stone-mid) 60%, var(--stone-dark));
  }
  .veil {
    position: absolute; left: 52px; top: 52px; width: 854px; height: 1096px;
    background: var(--veil); border-radius: 6px;
  }
  .veil-lower {
    position: absolute; left: 52px; top: 766px; width: 854px; height: 382px;
    background: var(--veil-strong); border-radius: 0 0 6px 6px;
  }
  .headline {
    position: absolute; left: 0; width: 958px; top: 122px; text-align: center;
    font-family: "Cinzel", "Times New Roman", serif; font-weight: 700; color: var(--alarm-red);
    font-variant: small-caps; line-height: 1.1;
  }
  .headline .fact { font-size: 36px; display: block; }
  .headline .question { font-size: 54px; display: block; margin-top: 14px; }
  .xray {
    position: absolute; left: 285px; top: 382px; width: 352px; height: 344px;
    background: radial-gradient(ellipse at 50% 50%, var(--xray-bone), #4a4a4a 45%, var(--xray-dark) 80%);
    border: 3px solid #2a2a2a;
  }
  .xray-caption {
    position: absolute; left: 0; width: 958px; top: 736px; text-align: center; font-size: 16px;
  }
  .offer {
    position: absolute; left: 0; width: 958px; top: 778px; text-align: center;
  }
  .brand-name {
    font-weight: 700; color: var(--brand-magenta); font-size: 36px; line-height: 1;
  }
  .brand-dot {
    display: inline-block; width: 16px; height: 16px; background: var(--brand-blue);
    border-radius: 50%; margin-left: 8px; vertical-align: middle;
  }
  .offer .intro { font-size: 13px; margin-top: 4px; color: var(--ink); }
  .offer .title { font-size: 34px; color: var(--hope-cyan); margin-top: 6px; }
  .offer .urge { font-size: 22px; color: var(--hope-cyan); margin-top: 6px; line-height: 1.3; }
  .rule { position: absolute; left: 150px; width: 658px; height: 2px; background: var(--ink); }
  .rule.top { top: 958px; }
  .rule.bottom { top: 1064px; }
  .contact-store { position: absolute; left: 153px; top: 966px; }
  .contact-store .brand-name { font-size: 28px; }
  .contact-store .brand-dot { width: 13px; height: 13px; }
  .contact-store address { font-style: normal; font-size: 23px; line-height: 1.2; margin-top: 4px; }
  .contact-call { position: absolute; left: 459px; top: 968px; }
  .contact-call .label { font-size: 32px; line-height: 1.15; }
  .contact-call .phone { font-size: 44px; line-height: 1.1; }
  .source-note {
    position: absolute; left: 0; width: 958px; top: 1074px; text-align: center;
    font-size: 11px; font-weight: 700; line-height: 1.4;
  }
</style>
</head>
<body>
<main class="flyer">
  <div class="stone-backdrop" role="img" aria-label="Cracked grey stone texture backdrop"></div>
  <div class="veil"></div>
  <div class="veil-lower"></div>

  <h1 class="headline">
    <span class="fact">Diabetes<br>Kills 3,400,000 People<br>In a Year</span>
    <span class="question">Are you the next?</span>
  </h1>

  <div class="xray" role="img" aria-label="Digital x-ray of a foot of a person with diabetes"></div>
  <p class="xray-caption">Digital foot xray of a person with diabetes</p>

  <section class="offer">
    <div class="brand-name">Oakline Pharmacy<span class="brand-dot"></span></div>
    <p class="intro">is offering</p>
    <h2 class="title">FREE Education for Diabetics</h2>
    <p class="urge">Call or Stop by Now! Your Life Depends on it!<br>Educate yourself and Live Longer</p>
  </section>

  <div class="rule top"></div>

  <div class="contact-store">
    <div class="brand-name">Oakline Pharmacy<span class="brand-dot"></span></div>
    <address>48-20 Maple Ave,<br>Kew Gardens&nbsp; NY 11415</address>
  </div>

  <div class="contact-call">
    <div class="label">Call now:</div>
    <div class="phone">(718) 555-0142</div>
  </div>

  <div class="rule bottom"></div>

  <p class="source-note">According to Global Health Survey in 2004, an estimated 3.4 million people died worldwide from consequences of high blood sugar.<br>Fact Sheet No. 312 (August,2011)</p>
</main>
</body>
</html>
```